2 guided dives on the North of Bonaire

2 guided shore dives on the North of Bonaire including authentic local lunch and drinks.
We offer an adventure for experienced divers to discover the dive sites on the north of the island.
Showing you the beauty of the reefs and tasting authentic local cuisine like goat or iguana combined with a stunning view of the surroundings.

Target Market(s)

Divers / tourism

Industry/Entity Type

Tourism / Diving

Font styles to use
Sans Serif

Colors
0054AA
0677BA
7BADD7
CADEEF
E8F1F8
0094D4
00A9DD
6FCCEA
C7EBF8
E9F6FB
F0912C
F2A743
F7CA91
FBE8D2
FDF5EE
EE7325
F08F49
F5BC92
FAE3D3
FDF4ED

Requirements
Must have
• Some of the pictures I uploaded and the food picture / bottom like in the pictures
Nice to have
• inviting to join us on the guided dives
Should not have
• Any picture I didn't provide

```html
<!DOCTYPE html>
<html lang="en">
<head>
<meta charset="utf-8">
<title>Guided Dives North Bonaire Flyer</title>
<link rel="stylesheet" href="https://fonts.googleapis.com/css2?family=Montserrat:wght@400;500;600;700&family=Yellowtail&display=swap">
<style>
  :root{
    --navy:#1f2c4f;
    --navy-deep:#242b45;
    --blue:#0054AA;
    --sky:#6FCCEA;
    --orange:#F2A743;
    --orange-deep:#F0912C;
    --paper:#ffffff;
    --mist:#eef1f5;
    --stage:#e6e8eb;
    --ink:#1f2c4f;
  }
  *{margin:0;padding:0;box-sizing:border-box}
  html,body{width:1050px;height:1200px;overflow:hidden;background:var(--stage)}
  body{font-family:"Montserrat",Arial,sans-serif;color:var(--ink)}
  .flyer{position:absolute;left:115px;top:20px;width:820px;height:1160px;overflow:hidden;background:var(--paper);box-shadow:0 4px 18px rgba(0,0,0,.18)}
  .flyer-shapes{position:absolute;inset:0}
  .brand{position:absolute;display:flex;align-items:center;gap:10px;color:var(--orange);font-weight:700;letter-spacing:.5px}
  .brand-top{left:540px;top:96px;font-size:30px}
  .brand-bottom{left:44px;top:1084px;font-size:19px;gap:7px}
  .brand-dot{border-radius:50%;background:var(--sky);flex:none}
  .brand-top .brand-dot{width:26px;height:26px}
  .brand-bottom .brand-dot{width:16px;height:16px}
  .headline{position:absolute;left:105px;top:255px;font-family:"Yellowtail",cursive;font-size:76px;line-height:.95;paint-order:stroke fill;-webkit-text-stroke:7px #fff;transform:rotate(-3deg)}
  .headline .line-a{display:block;color:var(--navy)}
  .headline .line-b{display:block;color:var(--orange-deep);margin-left:145px}
  .partner-badge{position:absolute;left:38px;top:488px;width:46px;height:46px;border-radius:50%;background:var(--blue)}
  .social{position:absolute;left:22px;top:586px;display:flex;gap:6px}
  .social span{width:38px;height:38px;border-radius:9px;background:var(--blue)}
  .social span+span{background:var(--orange-deep)}
  .offer-title{position:absolute;left:44px;top:652px;font-size:28px;font-weight:700;line-height:41px;letter-spacing:.3px;text-transform:uppercase}
  .offer-title em{font-style:normal;color:var(--orange-deep)}
  .perks{position:absolute;left:64px;top:800px;width:420px;list-style:none;font-size:21px;font-weight:500;line-height:27px}
  .perks li{position:relative;padding-left:26px;margin-bottom:14px}
  .perks li::before{content:"";position:absolute;left:0;top:11px;width:6px;height:6px;border-radius:50%;background:var(--ink)}
  .lunch{position:absolute;left:44px;top:912px;font-size:19px;font-weight:600;line-height:31px}
  .lunch em{font-style:normal;font-weight:700;font-size:23px;color:var(--orange-deep);text-transform:uppercase}
  .snapshot{position:absolute;background:#fff;padding:11px;box-shadow:0 4px 12px rgba(0,0,0,.28)}
  .snapshot div{width:100%;height:100%}
  .snapshot-food{left:560px;top:608px;width:200px;height:178px;transform:rotate(6deg)}
  .snapshot-food div{background:radial-gradient(circle at 35% 55%,#c0652b,#e3a05a 45%,#8a4a22 90%)}
  .snapshot-reef{left:590px;top:775px;width:200px;height:200px;transform:rotate(7deg)}
  .snapshot-reef div{background:linear-gradient(110deg,#5a2233 0%,#7a3040 28%,#1d6b86 45%,#2aa3c0 70%,#166b88 100%)}
  .footer-notes{position:absolute;top:1004px;left:166px;display:flex;gap:36px;color:#fff;font-size:12.5px;line-height:15px}
  .footer-notes p{position:relative;padding-left:15px;width:210px}
  .footer-notes p::before{content:"";position:absolute;left:0;top:3px;width:7px;height:7px;border-radius:50%;border:2px solid var(--orange)}
  .call-pill{position:absolute;left:211px;top:1063px;width:278px;height:30px;border-radius:5px;background:var(--orange);display:flex;align-items:center;gap:8px;padding-left:10px;font-size:17px;color:var(--navy);font-weight:500}
  .call-pill svg{width:17px;height:17px}
  .contact{position:absolute;left:503px;top:1066px;color:#fff;font-size:11px;line-height:20px}
  .contact p{display:flex;align-items:center;gap:7px}
  .contact i{width:11px;height:11px;border-radius:50%;background:var(--sky);display:inline-block}
  .web-band{position:absolute;left:211px;top:1108px;width:517px;height:29px;display:flex;font-size:22px}
  .web-band .label{width:258px;background:var(--orange);color:var(--navy);padding-left:26px;clip-path:polygon(0 0,100% 0,94% 100%,0 100%);line-height:29px}
  .web-band .url{flex:1;margin-left:-16px;background:#2f7fd0;color:#fff;text-align:center;line-height:29px;clip-path:polygon(6% 0,100% 0,100% 100%,0 100%)}
</style>
</head>
<body>
<main class="flyer">
  <svg class="flyer-shapes" width="820" height="1160" viewBox="0 0 820 1160">
    <defs>
      <linearGradient id="scene" x1="0" y1="0" x2="0.25" y2="1">
        <stop offset="0" stop-color="#9cc3e8"/>
        <stop offset="0.28" stop-color="#e9f6fb"/>
        <stop offset="0.36" stop-color="#1f6fb0"/>
        <stop offset="0.5" stop-color="#1fb3c8"/>
        <stop offset="0.7" stop-color="#cfd3cf"/>
        <stop offset="1" stop-color="#7a8a62"/>
      </linearGradient>
      <linearGradient id="mist" x1="0" y1="0" x2="1" y2="1">
        <stop offset="0" stop-color="#ffffff"/>
        <stop offset="1" stop-color="#e6eaf0"/>
      </linearGradient>
    </defs>
    <rect width="820" height="1160" fill="url(#mist)"/>
    <rect width="820" height="560" fill="var(--navy-deep)"/>
    <path d="M0,108 C300,90 620,170 820,330 L820,773 C560,740 200,620 0,443 Z" fill="url(#scene)" role="img" aria-label="Photo of a pebble beach and turquoise sea on the north coast of Bonaire"/>
    <path d="M0,108 C300,90 620,170 820,330 L820,560 C560,560 0,560 0,560 Z" fill="none"/>
    <path d="M0,443 C200,620 560,740 820,773 L820,1160 L0,1160 Z" fill="url(#mist)"/>
    <path d="M820,330 L820,773 C760,760 730,700 720,600 C710,450 740,350 820,330 Z" fill="var(--navy-deep)" opacity=".35"/>
    <path d="M300,100 C520,130 700,220 820,330" fill="none" stroke="var(--blue)" stroke-width="8" opacity=".8"/>
    <rect y="988" width="820" height="4" fill="var(--orange)"/>
    <rect y="994" width="820" height="166" fill="var(--navy)"/>
  </svg>

  <div class="brand brand-top"><span class="brand-dot"></span>Reefline Dive</div>

  <h1 class="headline"><span class="line-a">Let us Guide</span><span class="line-b">you!</span></h1>

  <div class="partner-badge"></div>
  <div class="social"><span></span><span></span></div>

  <h2 class="offer-title">2 Guided dives<br>at the <em>north side</em><br><em>of Bonaire</em></h2>
  <ul class="perks">
    <li>We show you the cool stuff</li>
    <li>You just enjoy the dives, we take care of the rest</li>
  </ul>
  <p class="lunch">Authentic local <em>Lunch and drinks</em><br>at Casa Vista Alta</p>

  <figure class="snapshot snapshot-food"><div role="img" aria-label="Photo of a plate of authentic local Bonaire food"></div></figure>
  <figure class="snapshot snapshot-reef"><div role="img" aria-label="Underwater photo of a seahorse on the reef"></div></figure>

  <div class="footer-notes">
    <p>Two guided dives at Klein Bonaire / North Coast</p>
    <p>Lunch, fruit, premium open bar and deluxe BBQ-diner is included</p>
  </div>

  <div class="brand brand-bottom"><span class="brand-dot"></span>Reefline Dive</div>

  <div class="call-pill">CALL US
    <svg viewBox="0 0 20 20"><circle cx="10" cy="10" r="9" fill="#fff" stroke="#1f2c4f" stroke-width="1.5"/><path d="M7 5.5l2 2-1 1.3c.6 1.3 1.6 2.3 2.9 2.9l1.3-1 2 2-1.3 1.5C9.5 14 6 10.5 5.5 7z" fill="#2f7fd0"/></svg>
    +(599) 555 01 23</div>

  <div class="contact">
    <p><i></i>Kaya Koral 12, Kralendijk, Bonaire</p>
    <p><i></i>info@reefline-dive.com</p>
  </div>

  <div class="web-band"><span class="label">Visit our website</span><span class="url">www.reefline-dive.com</span></div>
</main>
</body>
</html>
```